Changing the based bannders and pictures for template

9 Pictures have to be redesign for another product.
Its a template that I bought from the wesite. A website template. I like the pictures but I wanto change the text and product picture in the design.
I ad the pictures of the lighting. This is a example for the products I want. but just to give you a idea.
The font I really like to use the same and the color backgroud. Maybe a little bit different.
To give you a idea of the link of the template :
http://www.layoutvirex.com/demo/QRT274613/
also a Linke that I also like.
https://www.brontavia.nl/NL/Pages/Home.aspx

```html
<!DOCTYPE html>
<html lang="en">
<head>
<meta charset="utf-8">
<title>The Big Offer Day</title>
<link rel="stylesheet" href="https://fonts.googleapis.com/css2?family=Tinos:wght@400;700&family=Raleway:wght@700;800&display=swap">
<style>
  :root {
    --teal-deep: #1fb0b4;
    --teal-mid: #44c4c6;
    --teal-light: #8fe0db;
    --mist: #c9f1ec;
    --ink: #2b2b2b;
    --band: rgba(40, 120, 130, 0.45);
    --gold: #ffd23a;
    --white: #ffffff;
    --amber: #c0842e;
    --shade-white: #eceae4;
    --chrome: #a7b0b2;
  }
  * { margin: 0; padding: 0; box-sizing: border-box; }
  html, body { width: 1200px; height: 551px; overflow: hidden; }
  body { background: var(--teal-mid); }

  .banner {
    position: relative;
    width: 1200px;
    height: 551px;
    overflow: hidden;
    background:
      radial-gradient(ellipse 380px 300px at 400px 320px, var(--mist) 0%, rgba(201,241,236,0) 100%),
      radial-gradient(ellipse 500px 260px at 420px 560px, var(--teal-light) 0%, rgba(143,224,219,0) 100%),
      linear-gradient(160deg, var(--teal-deep) 0%, var(--teal-mid) 45%, var(--teal-light) 75%, var(--teal-mid) 100%);
  }

  .product-visual {
    position: absolute;
    left: 80px;
    top: 92px;
    width: 470px;
    height: 432px;
    border-radius: 6px;
    background: linear-gradient(180deg, var(--amber) 0%, var(--shade-white) 45%, var(--chrome) 100%);
  }

  .offer {
    position: absolute;
    left: 612px;
    top: 180px;
    width: 512px;
    text-align: center;
  }

  .offer__title {
    font-family: "Tinos", "Times New Roman", serif;
    font-size: 72px;
    line-height: 1;
    color: var(--ink);
    letter-spacing: -2.5px;
    font-weight: 400;
    white-space: nowrap;
  }
  .offer__title strong { font-weight: 700; }

  .offer__band {
    display: block;
    margin: 27px auto 0;
    width: 400px;
    height: 45px;
    background: var(--band);
    font-family: "Raleway", Arial, sans-serif;
    font-weight: 800;
    font-size: 23px;
    line-height: 45px;
    color: var(--gold);
    letter-spacing: 0.2px;
  }

  .offer__note {
    margin-top: 17px;
    font-family: "Raleway", Arial, sans-serif;
    font-weight: 800;
    font-size: 21px;
    color: var(--white);
    letter-spacing: 0.2px;
  }
</style>
</head>
<body>
  <main class="banner">
    <div class="product-visual" role="img" aria-label="Product photo: two table lamps with amber and white glass shades on chrome tripod legs, reflected on a glossy surface"></div>

    <section class="offer">
      <h1 class="offer__title"><strong>The Big</strong> Offer Day</h1>
      <p class="offer__band">EXTRA 20% OFF</p>
      <p class="offer__note">ON SELECTED LIGHTING</p>
    </section>
  </main>
</body>
</html>
```